Want a package created for a new protein bar

We would like a new package created for a new protein bar project The name of the bar will be VORNBar a real food protein bar, we would like a ‘window’ on the package of bar like Brisk Mell bar below in images.

VORNBar
‘Super Food Bar’
14g of Whey Protein
The package film size is the following 12cm width x 15cm Length,
Flavor Peanut Chocolate Chip, additional information will be attached shortly like nutrition facts,

Target Market(s)

fitness market, bodybuilders, athletes, everyday people

Industry/Entity Type

Health Product

Logo Text

VORNBar

Font styles to use
Serif
Sans Serif
Decorative

Requirements
Must have
• Package window

```html
<!DOCTYPE html>
<html lang="en">
<head>
<meta charset="utf-8">
<title>VORNBar – Super Food Bar wrappers</title>
<link href="https://fonts.googleapis.com/css2?family=Archivo+Black&family=Oswald:wght@400;500;600&display=swap" rel="stylesheet">
<style>
  :root {
    --stage: #2b2b2b;
    --ink: #0b0b0b;
    --white: #ffffff;
    --grape: #4b1f4c;
    --grape-light: #6a2f6b;
    --amber: #f0a11b;
    --amber-light: #f7cf2a;
    --navy: #1e3452;
    --navy-light: #2f4d73;
    --window-frame: rgba(200, 200, 200, 0.35);
    --bar-brown: #8a5a2b;
    --bar-gold: #d9a24c;
    --peanut: #c9a077;
    --cocoa: #4a2a1a;
  }
  * { box-sizing: border-box; margin: 0; padding: 0; }
  html, body { width: 1200px; height: 941px; overflow: hidden; }
  body { background: var(--stage); position: relative; }

  .wrapper {
    position: absolute;
    width: 792px;
    height: 288px;
    background: linear-gradient(180deg, var(--tone-light) 0%, var(--tone) 35%, var(--tone) 75%, var(--tone-light) 100%);
    clip-path: polygon(8px 0, 784px 0, 792px 8px, 784px 16px, 792px 24px, 784px 32px, 792px 40px, 784px 48px, 792px 56px, 784px 64px, 792px 72px, 784px 80px, 792px 88px, 784px 96px, 792px 104px, 784px 112px, 792px 120px, 784px 128px, 792px 136px, 784px 144px, 792px 152px, 784px 160px, 792px 168px, 784px 176px, 792px 184px, 784px 192px, 792px 200px, 784px 208px, 792px 216px, 784px 224px, 792px 232px, 784px 240px, 792px 248px, 784px 256px, 792px 264px, 784px 272px, 792px 280px, 784px 288px, 8px 288px, 0 280px, 8px 272px, 0 264px, 8px 256px, 0 248px, 8px 240px, 0 232px, 8px 224px, 0 216px, 8px 208px, 0 200px, 8px 192px, 0 184px, 8px 176px, 0 168px, 8px 160px, 0 152px, 8px 144px, 0 136px, 8px 128px, 0 120px, 8px 112px, 0 104px, 8px 96px, 0 88px, 8px 80px, 0 72px, 8px 64px, 0 56px, 8px 48px, 0 40px, 8px 32px, 0 24px, 8px 16px, 0 8px);
  }
  .wrapper--grape { --tone: var(--grape); --tone-light: var(--grape-light); left: 77px; top: 30px; }
  .wrapper--amber { --tone: var(--amber); --tone-light: var(--amber-light); left: 225px; top: 318px; }
  .wrapper--navy  { --tone: var(--navy);  --tone-light: var(--navy-light);  left: 361px; top: 604px; }

  .brand {
    position: absolute;
    left: 124px; top: 144px;
    transform: translate(-50%, -50%) rotate(-90deg);
    font-family: "Archivo Black", sans-serif;
    font-size: 42px;
    line-height: 1;
    color: var(--white);
    white-space: nowrap;
    letter-spacing: -1px;
  }

  .window {
    position: absolute;
    left: 163px; top: 26px;
    width: 115px; height: 236px;
    background: var(--window-frame);
  }
  .window__contents {
    position: absolute;
    left: 0; right: 0; top: 22px; bottom: 22px;
    background: linear-gradient(160deg, var(--bar-gold) 0%, var(--bar-brown) 45%, var(--bar-gold) 70%, var(--bar-brown) 100%);
  }

  .headline {
    position: absolute;
    z-index: 3;
    left: 298px; top: 44px;
    width: 266px; height: 124px;
    background: var(--ink);
    border-radius: 6px 10px 4px 12px;
    transform: rotate(-1deg);
    color: var(--white);
    font-family: "Archivo Black", sans-serif;
    text-align: center;
    padding-top: 10px;
  }
  .headline__top { display: block; font-size: 54px; line-height: 56px; letter-spacing: -1px; }
  .headline__bottom { display: block; font-size: 40px; line-height: 44px; letter-spacing: -1px; }

  .flavor {
    position: absolute;
    z-index: 3;
    left: 326px; top: 185px;
    width: 108px; height: 38px;
    background: var(--white);
    border-radius: 3px;
    color: var(--ink);
    font-family: "Oswald", sans-serif;
    font-weight: 500;
    font-size: 13px;
    line-height: 15px;
    padding: 4px 0 0 9px;
    white-space: nowrap;
  }

  .ingredients {
    position: absolute;
    z-index: 2;
    left: 442px; top: 174px;
    width: 240px; height: 86px;
    border-radius: 40px 50px 40px 36px;
    background: radial-gradient(ellipse at 40% 60%, var(--cocoa) 0%, var(--peanut) 30%, var(--peanut) 70%, transparent 100%);
  }

  .protein {
    position: absolute;
    z-index: 1;
    left: 604px; top: 26px;
    width: 102px; height: 236px;
    background: var(--ink);
    color: var(--white);
    font-family: "Oswald", sans-serif;
    text-align: center;
  }
  .protein__amount { display: block; margin-top: 18px; font-size: 56px; font-weight: 600; line-height: 60px; }
  .protein__label { display: block; font-size: 16px; font-weight: 500; line-height: 18px; }
</style>
</head>
<body>

  <div class="wrapper wrapper--grape">
    <span class="brand">VORNBar</span>
    <div class="window"><div class="window__contents" role="img" aria-label="View of the nut and chocolate bar through the clear window"></div></div>
    <div class="protein"><span class="protein__amount">14G</span><span class="protein__label">OF WHEY<br>PROTEIN</span></div>
    <div class="ingredients" role="img" aria-label="Peanuts in shell with a leaf and a chocolate curl"></div>
    <div class="headline"><span class="headline__top">SUPER</span><span class="headline__bottom">FOOD BAR</span></div>
    <div class="flavor">FLAVOR PEANUT<br>CHOCOLATE CHIP</div>
  </div>

  <div class="wrapper wrapper--amber">
    <span class="brand">VORNBar</span>
    <div class="window"><div class="window__contents" role="img" aria-label="View of the nut and chocolate bar through the clear window"></div></div>
    <div class="protein"><span class="protein__amount">14G</span><span class="protein__label">OF WHEY<br>PROTEIN</span></div>
    <div class="ingredients" role="img" aria-label="Peanuts in shell with a leaf and a chocolate curl"></div>
    <div class="headline"><span class="headline__top">SUPER</span><span class="headline__bottom">FOOD BAR</span></div>
    <div class="flavor">FLAVOR PEANUT<br>CHOCOLATE CHIP</div>
  </div>

  <div class="wrapper wrapper--navy">
    <span class="brand">VORNBar</span>
    <div class="window"><div class="window__contents" role="img" aria-label="View of the nut and chocolate bar through the clear window"></div></div>
    <div class="protein"><span class="protein__amount">14G</span><span class="protein__label">OF WHEY<br>PROTEIN</span></div>
    <div class="ingredients" role="img" aria-label="Peanuts in shell with a leaf and a chocolate curl"></div>
    <div class="headline"><span class="headline__top">SUPER</span><span class="headline__bottom">FOOD BAR</span></div>
    <div class="flavor">FLAVOR PEANUT<br>CHOCOLATE CHIP</div>
  </div>

</body>
</html>
```